Desk Allies Business Card

Contact Information for Business Card

Janne Voutilainen
Managing Director

3/47 Brindle Street Larkfield ACT 2915

Tel: +61 02 6257 3140
Mob: +61 0427 315 846

Email: janne@deskallies.com.au
Web: www.deskallies.com.au

Colors

Designer to choose colors to be used in the design.

Requirements
Must have
• Logo, Name, Title, Address, Telephone, Mobile, Email Address and Website
• "Desk Ally International Pty Ltd"

```html
<!DOCTYPE html>
<html lang="en">
<head>
<meta charset="utf-8">
<title>Desk Allies Business Card</title>
<link rel="stylesheet" href="https://fonts.googleapis.com/css2?family=Montserrat:wght@400;700&family=Marcellus&family=Open+Sans:wght@600&display=swap">
<style>
  :root {
    --brand-blue: #1b75bb;
    --ink: #231f20;
    --tagline-grey: #4d4d4f;
    --faint-grey: #e6e7e8;
    --card-border: #dcdcdc;
    --paper: #ffffff;
  }
  * { margin: 0; padding: 0; box-sizing: border-box; }
  html, body { width: 992px; height: 1200px; overflow: hidden; background: var(--paper); }
  .canvas { position: relative; width: 992px; height: 1200px; }

  .card { position: absolute; overflow: hidden; }

  /* Front */
  .card-front {
    left: 119px; top: 143px; width: 749px; height: 428px;
    background: var(--paper); border: 1px solid var(--card-border);
  }
  .front-accent {
    position: absolute; left: 660px; top: 66px; width: 240px; height: 240px;
    border-radius: 50%; background: var(--faint-grey);
  }
  .brand-dot {
    position: absolute; left: 108px; top: 114px; width: 96px; height: 96px;
    border-radius: 50%; background: var(--brand-blue);
  }
  .brand-name {
    position: absolute; left: 224px; top: 126px;
    font-family: "Montserrat", sans-serif; font-weight: 700; font-size: 40px;
    color: var(--brand-blue); letter-spacing: 0.5px; line-height: 1; white-space: nowrap;
  }
  .brand-tagline {
    position: absolute; left: 225px; top: 174px;
    font-family: "Montserrat", sans-serif; font-weight: 400; font-size: 14.5px;
    color: var(--tagline-grey); letter-spacing: 5px; white-space: nowrap;
  }
  .person-name {
    position: absolute; left: 0; right: 0; top: 230px; text-align: center;
    font-family: "Marcellus", serif; font-weight: 400; font-size: 41px; color: var(--brand-blue); line-height: 1.1;
  }
  .person-title {
    position: absolute; left: 0; right: 0; top: 280px; text-align: center;
    font-family: "Marcellus", serif; font-weight: 400; font-size: 24px; color: var(--ink);
  }
  .contact-line {
    position: absolute; left: 0; right: 0; top: 349px; text-align: center;
    font-family: "Open Sans", sans-serif; font-weight: 600; font-size: 23px; color: var(--ink);
    white-space: nowrap;
  }
  .contact-line .divider { margin: 0 10px; }
  .contact-line .email { color: var(--brand-blue); }

  /* Back */
  .card-back {
    left: 124px; top: 611px; width: 748px; height: 427px;
    background: var(--brand-blue);
  }
  .back-dot {
    position: absolute; left: 31px; top: 54px; width: 230px; height: 230px;
    border-radius: 50%; background: var(--paper);
  }
  .company-name {
    position: absolute; left: 291px; top: 160px;
    font-family: "Open Sans", sans-serif; font-weight: 600; font-size: 23px; color: var(--paper);
    white-space: nowrap;
  }
  .company-details {
    position: absolute; right: 46px; top: 288px; text-align: right;
    font-family: "Open Sans", sans-serif; font-style: normal; font-weight: 600; font-size: 22px; line-height: 29px;
    color: var(--paper); white-space: nowrap;
  }
</style>
</head>
<body>
<main class="canvas">
  <section class="card card-front" aria-label="Business card front">
    <div class="front-accent" aria-hidden="true"></div>
    <div class="brand-dot" aria-hidden="true"></div>
    <div class="brand-name">DESK ALLIES</div>
    <div class="brand-tagline">ADAPTIVE WORKPLACE INTERIORS</div>
    <h1 class="person-name">Janne Voutilainen</h1>
    <p class="person-title">Managing Director</p>
    <p class="contact-line">Mob: +61 0427 315 846<span class="divider">|</span>Email: <span class="email">janne@deskallies.com.au</span></p>
  </section>

  <section class="card card-back" aria-label="Business card back">
    <div class="back-dot" aria-hidden="true"></div>
    <p class="company-name">Desk Ally International Pty Ltd</p>
    <address class="company-details">
      3/47 Brindle Street Larkfield ACT 2915<br>
      Tel: +61 02 6257 3140<br>
      www.deskallies.com.au
    </address>
  </section>
</main>
</body>
</html>
```